Design some Business Cards for NBW

Need a business card using logo attached. Looking for clean professional look for a wholesale lighting distributor. Needs to have below info.

Tobin Marrow
3817 Fenwood St Suite 204
Ashbury Glen, Co 80473
ph 800.316.2297
fx 800.481.6630
tobin@nordanebeam.com
nordanebeam.com

```html
<!DOCTYPE html>
<html lang="en">
<head>
<meta charset="utf-8">
<title>NBW Business Card</title>
<link rel="stylesheet" href="https://fonts.googleapis.com/css2?family=Open+Sans:wght@400;600&display=swap">
<style>
  :root {
    --bg: #e6e6e6;
    --card-dark: #2c2c2c;
    --card-white: #ffffff;
    --ink: #3a3a3a;
    --muted: #9a9a9a;
    --brand-blue: #2f8fcf;
    --link-blue: #2a9ad6;
    --tab-red: #d8232a;
    --tab-orange: #f07f1d;
    --tab-green: #8cc63f;
    --tab-blue: #1b87cf;
  }
  * { margin: 0; padding: 0; box-sizing: border-box; }
  html, body { width: 1200px; height: 960px; overflow: hidden; }
  body {
    background: var(--bg);
    font-family: "Open Sans", Arial, sans-serif;
    color: var(--ink);
    position: relative;
  }
  .card {
    position: absolute;
    left: 250px;
    width: 700px;
    height: 400px;
    overflow: hidden;
    box-shadow: 0 6px 18px rgba(0,0,0,0.18);
  }
  .card--front { top: 60px; background: var(--card-white); }
  .card--back { top: 500px; background: var(--card-dark); }

  /* front */
  .front__dark {
    position: absolute; left: 0; top: 0;
    width: 390px; height: 400px;
    background: var(--card-dark);
  }
  .brand {
    position: absolute;
    display: flex; align-items: center; gap: 14px;
  }
  .brand__mark {
    width: 34px; height: 34px;
    background: var(--brand-blue);
    flex: none;
  }
  .brand__text { display: flex; flex-direction: column; }
  .brand__name {
    font-size: 21px; font-weight: 400;
    color: var(--brand-blue);
    letter-spacing: 0.5px; line-height: 1.1;
    text-transform: uppercase;
    white-space: nowrap;
  }
  .brand__tagline {
    font-size: 11px; color: var(--muted);
    margin-top: 4px; letter-spacing: 0.3px;
  }
  .card--front .brand { left: 40px; top: 172px; }

  .info-tabs {
    position: absolute; left: 362px; top: 34px;
    width: 58px;
    display: flex; flex-direction: column;
  }
  .info-tab {
    height: 58px;
    display: flex; align-items: center; justify-content: center;
  }
  .info-tab svg { width: 26px; height: 26px; fill: #fff; }
  .info-tab--red { background: var(--tab-red); }
  .info-tab--orange { background: var(--tab-orange); }
  .info-tab--green { background: var(--tab-green); }
  .info-tab--blue { background: var(--tab-blue); height: 62px; }
  .info-tab--blue svg { fill: none; stroke: #fff; stroke-width: 1.8; }

  .contact {
    position: absolute; left: 445px; top: 50px;
    font-size: 14px; line-height: 1.45;
    white-space: nowrap;
  }
  .contact__name { font-size: 20px; font-weight: 400; margin-bottom: 24px; }
  .contact__block { margin-bottom: 22px; }
  .contact__email { color: var(--link-blue); }

  /* back */
  .back__panel {
    position: absolute; left: 52px; top: 0;
    width: 596px; height: 400px;
    background: var(--card-white);
  }
  .edge-tabs {
    position: absolute; top: 52px;
    width: 42px;
    display: flex; flex-direction: column;
  }
  .edge-tabs--left { left: 34px; }
  .edge-tabs--right { right: 34px; top: 130px; }
  .edge-tabs span { height: 56px; display: block; }
  .edge-tabs .t-red { background: var(--tab-red); }
  .edge-tabs .t-orange { background: var(--tab-orange); }
  .edge-tabs .t-green { background: var(--tab-green); }
  .edge-tabs .t-blue { background: var(--tab-blue); height: 62px; }
  .card--back .brand { left: 175px; top: 168px; }
  .card--back .brand__name { font-size: 24px; }
</style>
</head>
<body>

<section class="card card--front" aria-label="Business card front">
  <div class="front__dark"></div>
  <div class="brand">
    <div class="brand__mark"></div>
    <div class="brand__text">
      <span class="brand__name">Nordane Beam Works</span>
      <span class="brand__tagline">wholesale lighting supply</span>
    </div>
  </div>

  <div class="info-tabs">
    <div class="info-tab info-tab--red">
      <svg viewBox="0 0 24 24" aria-hidden="true"><circle cx="12" cy="8" r="4.5"/><path d="M3 22c0-5 4-8 9-8s9 3 9 8z"/></svg>
    </div>
    <div class="info-tab info-tab--orange">
      <svg viewBox="0 0 24 24" aria-hidden="true"><path d="M12 3 2 12h3v9h5v-6h4v6h5v-9h3z"/></svg>
    </div>
    <div class="info-tab info-tab--green">
      <svg viewBox="0 0 24 24" aria-hidden="true"><path d="M6.6 10.8a15 15 0 0 0 6.6 6.6l2.2-2.2a1 1 0 0 1 1-.25 11.4 11.4 0 0 0 3.6.57 1 1 0 0 1 1 1V20a1 1 0 0 1-1 1A17 17 0 0 1 3 4a1 1 0 0 1 1-1h3.5a1 1 0 0 1 1 1c0 1.25.2 2.45.57 3.57a1 1 0 0 1-.25 1z"/></svg>
    </div>
    <div class="info-tab info-tab--blue">
      <svg viewBox="0 0 24 24" aria-hidden="true"><circle cx="12" cy="12" r="9"/><ellipse cx="12" cy="12" rx="4" ry="9"/><path d="M3 12h18M5 7h14M5 17h14"/></svg>
    </div>
  </div>

  <div class="contact">
    <p class="contact__name">Tobin Marrow</p>
    <div class="contact__block">
      <p>3817 Fenwood St Suite 204</p>
      <p>Ashbury Glen, Co 80473</p>
    </div>
    <div class="contact__block">
      <p>800.316.2297</p>
      <p>800.481.6630</p>
    </div>
    <div>
      <p class="contact__email">tobin@nordanebeam.com</p>
      <p>nordanebeam.com</p>
    </div>
  </div>
</section>

<section class="card card--back" aria-label="Business card back">
  <div class="back__panel"></div>
  <div class="edge-tabs edge-tabs--left">
    <span class="t-red"></span><span class="t-orange"></span><span class="t-green"></span><span class="t-blue"></span>
  </div>
  <div class="edge-tabs edge-tabs--right">
    <span class="t-red"></span><span class="t-orange"></span><span class="t-green"></span><span class="t-blue"></span>
  </div>
  <div class="brand">
    <div class="brand__mark"></div>
    <div class="brand__text">
      <span class="brand__name">Nordane Beam Works</span>
      <span class="brand__tagline">wholesale lighting supply</span>
    </div>
  </div>
</section>

</body>
</html>
```